Logo and Business Card for Dental Office

We are opening a periodontal office (dental specialist for dental implants and gum diseases). It is a brand new state of the art facility with a focus on the most effective treatments for retaining natural teeth, or replacing teeth with implants when they must be lost. Strong emphasis on customer service and amenities for patient comfort. We are located just outside of Boston, MA.

Target Market(s)

potential adult patients, dentists in the community that will refer patients for specialized care

Industry/Entity Type

Dental

Requirements
Must have
• business name, address, phone number, website
Marcus T. Velloran, DMD LLC
274 Kestrel Lane, Ste 305
Linden Falls, NH 03842
603-555-0172
603-555-0189 Fax
DrVelloran-example.com

the uploaded file has a rough version of what I'm looking for in the logo, I like the colors but it can be varies some.
Nice to have
• simple logo or symbol on business card, one possible idea I had was an abstract symbol of a screw or threads that might represent a dental implant, the attached file gives an idea of where to start.
Should not have
• I want a professional feel, no cartoons of teeth that appear childish, etc
The font should be easy to read with no curly/swirly shapes.

```html
<!DOCTYPE html>
<html lang="en">
<head>
<meta charset="utf-8">
<title>Marcus T. Velloran — Business Card</title>
<link rel="stylesheet" href="https://fonts.googleapis.com/css2?family=Roboto+Slab:wght@300;400&display=swap">
<style>
  :root {
    --navy: #222d63;
    --red: #d12a36;
    --white: #ffffff;
    --paper: #ececec;
    --ink-light: #e8eaf4;
  }
  * { margin: 0; padding: 0; box-sizing: border-box; }
  html, body {
    width: 1200px;
    height: 794px;
    overflow: hidden;
    background: var(--paper);
    font-family: "Roboto Slab", "Rockwell", Georgia, serif;
  }
  .canvas {
    position: relative;
    width: 1200px;
    height: 794px;
  }
  .card {
    position: absolute;
    top: 254px;
    width: 504px;
    height: 288px;
    box-shadow: 0 6px 18px rgba(0, 0, 0, 0.12);
  }
  .card--front {
    left: 66px;
    background: var(--white);
  }
  .card--back {
    left: 630px;
    background: var(--navy);
    color: var(--ink-light);
  }

  /* Front: name lockup */
  .lockup {
    position: absolute;
    left: 50%;
    top: 50%;
    transform: translate(-50%, -50%);
    display: flex;
    flex-direction: column;
    align-items: flex-end;
  }
  .lockup__name-row {
    display: flex;
    align-items: center;
    gap: 14px;
  }
  .lockup__mark {
    width: 18px;
    height: 18px;
    border-radius: 50%;
    background: var(--red);
  }
  .lockup__name {
    font-weight: 400;
    font-size: 40px;
    letter-spacing: 0.5px;
    color: var(--navy);
    white-space: nowrap;
  }
  .lockup__tagline {
    margin-top: 6px;
    font-weight: 300;
    font-size: 15px;
    color: var(--navy);
    letter-spacing: 0.3px;
  }
  .lockup__tagline .accent { color: var(--red); }

  /* Back: contact details */
  .contact {
    position: absolute;
    left: 44px;
    top: 40px;
    font-style: normal;
    font-weight: 300;
    font-size: 14px;
    line-height: 1.55;
    letter-spacing: 0.3px;
  }
  .contact__block { margin-bottom: 6px; }
  .contact__label {
    display: inline-block;
    width: 34px;
    color: var(--red);
    font-weight: 400;
  }
  .contact__web { margin-top: 6px; }
</style>
</head>
<body>
<main class="canvas">
  <section class="card card--front" aria-label="Business card front">
    <div class="lockup">
      <div class="lockup__name-row">
        <span class="lockup__mark" aria-hidden="true"></span>
        <span class="lockup__name">Marcus T. Velloran</span>
      </div>
      <p class="lockup__tagline"><span class="accent">Periodontics</span> &amp; Dental Implants</p>
    </div>
  </section>

  <section class="card card--back" aria-label="Business card back">
    <address class="contact">
      <div class="contact__block">
        Marcus T. Velloran, DMD LLC<br>
        274 Kestrel Lane, Ste 305<br>
        Linden Falls, NH 03842
      </div>
      <div class="contact__block">
        <span class="contact__label">Tel</span>: 603 - 555 - 0172<br>
        <span class="contact__label">Fax</span>: 603 - 555 - 0189
      </div>
      <div class="contact__web">www.drvelloran-example.com</div>
    </address>
  </section>
</main>
</body>
</html>
```